Tova Brisk Fitness Coaching Project

I am a personal trainer based in London. My services include one-on-one PT sessions, bootcamps.
I would like the design to be minimalistic. With light colours: white, pink, purple.
I specialise in weight loss, flexibility, mobility.

Tova Penrick
Personal Trainer
Email: tova.penrick@mailgrove.net
tel: 07500 918 243
Instagram: Tova Brisk

Target Market(s)

adults, mostly females (age 18-50).

Industry/Entity Type

Fitness

Contact Information for Business Card

Tova Penrick
Personal Trainer
tel: 07500 918 243
Instagram: Tova Brisk

Font styles to use
Serif

Colors
eea4c8
fbd4d5
fdf9cf
cfeae6
cee9f5

Requirements
Nice to have
• minimalistic style
• easy to read and remember

```html
<!DOCTYPE html>
<html lang="en">
<head>
<meta charset="utf-8">
<title>Tova Penrick – Personal Trainer Business Card</title>
<link rel="stylesheet" href="https://fonts.googleapis.com/css2?family=Josefin+Sans:wght@300;400;600&display=swap">
<style>
  :root {
    --backdrop: #d9d9d9;
    --card-white: #ffffff;
    --sun-yellow: #fdf9cf;
    --sun-blush: #fbd4d5;
    --brand-pink: #eea4c8;
    --ink-grey: #555555;
    --text-dark: #2b2b2b;
  }
  * { margin: 0; padding: 0; box-sizing: border-box; }
  html, body {
    width: 1200px;
    height: 800px;
    overflow: hidden;
    background: var(--backdrop);
    font-family: "Josefin Sans", sans-serif;
  }
  .card-sheet {
    width: 1200px;
    height: 800px;
    display: flex;
    align-items: center;
    justify-content: center;
    gap: 40px;
  }
  .card {
    position: relative;
    width: 525px;
    height: 300px;
    overflow: hidden;
    box-shadow: 0 4px 14px rgba(0, 0, 0, 0.18);
  }

  /* Front */
  .card-front { background: var(--sun-yellow); }
  .sunburst {
    position: absolute;
    inset: 0;
    background:
      radial-gradient(circle at 50% 42%, rgba(251, 212, 213, 0.95) 0%, rgba(251, 212, 213, 0.55) 22%, rgba(253, 249, 207, 0) 60%),
      var(--sun-yellow);
  }
  .brand {
    position: absolute;
    left: 0; right: 0;
    top: 50%;
    transform: translateY(-50%);
    display: flex;
    flex-direction: column;
    align-items: center;
  }
  .brand-row {
    display: flex;
    align-items: center;
    gap: 12px;
  }
  .brand-dot {
    width: 22px;
    height: 22px;
    border-radius: 50%;
    background: var(--brand-pink);
  }
  .brand-name {
    font-weight: 600;
    font-size: 34px;
    letter-spacing: 1px;
    color: var(--brand-pink);
    text-transform: uppercase;
    line-height: 1;
  }
  .brand-role {
    margin-top: 8px;
    font-weight: 400;
    font-size: 13px;
    letter-spacing: 2px;
    color: var(--ink-grey);
    text-transform: uppercase;
  }
  .card-front .brand { top: 52%; }

  /* Back */
  .card-back { background: var(--card-white); }
  .card-back .brand {
    left: 40px;
    right: auto;
    top: auto;
    bottom: 42px;
    transform: none;
    align-items: flex-start;
  }
  .card-back .brand-name { font-size: 26px; }
  .card-back .brand-dot { width: 18px; height: 18px; }
  .card-back .brand-role { font-size: 11px; margin-left: 30px; }

  .contact-list {
    position: absolute;
    top: 40px;
    right: 38px;
    list-style: none;
    display: flex;
    flex-direction: column;
    gap: 14px;
  }
  .contact-item {
    display: flex;
    align-items: center;
    gap: 14px;
    font-size: 16px;
    font-weight: 300;
    color: var(--text-dark);
  }
  .contact-icon {
    width: 26px;
    height: 26px;
    flex: none;
  }
</style>
</head>
<body>
<main class="card-sheet">

  <section class="card card-front" aria-label="Business card front">
    <div class="sunburst" role="img" aria-label="Soft pink sunburst rays on pale yellow"></div>
    <div class="brand">
      <div class="brand-row">
        <span class="brand-dot"></span>
        <span class="brand-name">Tova Penrick</span>
      </div>
      <span class="brand-role">Personal Trainer</span>
    </div>
  </section>

  <section class="card card-back" aria-label="Business card back">
    <ul class="contact-list">
      <li class="contact-item">
        <svg class="contact-icon" viewBox="0 0 26 26" aria-hidden="true">
          <circle cx="13" cy="13" r="13" fill="#eea4c8"/>
          <path d="M8 9.5c0 5 3.5 8.5 8.5 8.5l1.5-2-2.5-1.5-1.2 1c-1.8-.8-3-2-3.8-3.8l1-1.2L10 8z" fill="#ffffff"/>
        </svg>
        <span>07500 918 243</span>
      </li>
      <li class="contact-item">
        <svg class="contact-icon" viewBox="0 0 26 26" aria-hidden="true">
          <circle cx="13" cy="13" r="13" fill="#eea4c8"/>
          <rect x="7" y="9" width="12" height="8.5" rx="1" fill="none" stroke="#ffffff" stroke-width="1.4"/>
          <path d="M7.5 9.5 13 14l5.5-4.5" fill="none" stroke="#ffffff" stroke-width="1.4"/>
        </svg>
        <span>tova.penrick@mailgrove.net</span>
      </li>
      <li class="contact-item">
        <svg class="contact-icon" viewBox="0 0 26 26" aria-hidden="true">
          <circle cx="13" cy="13" r="13" fill="#eea4c8"/>
        </svg>
        <span>Tova Brisk</span>
      </li>
    </ul>
    <div class="brand">
      <div class="brand-row">
        <span class="brand-dot"></span>
        <span class="brand-name">Tova Penrick</span>
      </div>
      <span class="brand-role">Personal Trainer</span>
    </div>
  </section>

</main>
</body>
</html>
```